Thornquist Landscaping buisness cards.

There's no existing logo andthis is a new landscaping buisness looking for a complete card design. Would like the logo and name to take up one side.

Target Market(s)

Professionals, Middle aged, Elderly.

Industry/Entity Type

Landscaping

Contact Information for Business Card

Thornquist Landscaping
Malcolm Thornquist (owner)
555-782-4610
Malcolmrthornquist@fernmail.example

Font styles to use
Sans Serif

Colors
9bcb3c
0555a3
ec1f27

Requirements
Must have
• Easy to read print and contact information, all capital letters
Nice to have
• Colored backdrop
Should not have
• Pictures of lawnmowers.

```html
<!DOCTYPE html>
<html lang="en">
<head>
<meta charset="utf-8">
<title>Thornquist Landscaping – Business Cards</title>
<link href="https://fonts.googleapis.com/css2?family=Open+Sans:wght@300;400;600;700;800&display=swap" rel="stylesheet">
<style>
  :root {
    --bg: #d4d4d4;
    --card-white: #ffffff;
    --green: #5bbd2b;
    --green-light: #7fd63a;
    --green-pale: #9bd05a;
    --ink: #3a3d42;
    --white: #ffffff;
  }
  * { margin: 0; padding: 0; box-sizing: border-box; }
  html, body {
    width: 1200px; height: 1064px; overflow: hidden;
    background: var(--bg);
    font-family: "Open Sans", Arial, sans-serif;
  }
  .sheet {
    position: relative; width: 1200px; height: 1064px;
    display: flex; flex-direction: column; align-items: center; justify-content: center; gap: 60px;
  }
  .card {
    position: relative; width: 720px; height: 411px; overflow: hidden;
    box-shadow: 0 14px 30px rgba(0,0,0,.18);
  }

  /* Front */
  .card-front { background: var(--card-white); }
  .front-swoosh { position: absolute; inset: 0; width: 100%; height: 100%; }
  .brand {
    position: absolute; left: 90px; top: 150px;
    display: flex; align-items: center; gap: 22px;
  }
  .brand-dot { width: 54px; height: 54px; border-radius: 50%; background: var(--green); flex: none; }
  .brand-name {
    font-weight: 800; font-size: 40px; line-height: 1.05; color: var(--ink);
    text-transform: uppercase; letter-spacing: .5px;
  }

  /* Back */
  .card-back {
    background: radial-gradient(ellipse at 35% 30%, var(--green-light), var(--green) 70%);
    color: var(--white);
  }
  .owner { position: absolute; left: 48px; top: 52px; }
  .owner-name { font-weight: 700; font-size: 28px; letter-spacing: .5px; text-transform: uppercase; }
  .owner-rule { display: flex; align-items: center; gap: 12px; margin-top: 4px; }
  .owner-rule span { display: block; width: 120px; height: 1.5px; background: var(--white); }
  .owner-title { font-weight: 300; font-size: 17px; letter-spacing: 7px; text-transform: uppercase; }
  .back-decoration {
    position: absolute; right: 0; top: 0; width: 250px; height: 100%;
  }
  .contact {
    position: absolute; left: 48px; bottom: 58px;
    list-style: none; font-size: 16px; font-weight: 600; letter-spacing: .3px;
    text-transform: uppercase;
  }
  .contact li { display: flex; align-items: center; gap: 10px; margin-top: 8px; white-space: nowrap; }
  .contact svg { width: 20px; height: 20px; flex: none; }
</style>
</head>
<body>
<main class="sheet">

  <section class="card card-front" aria-label="Card front">
    <svg class="front-swoosh" viewBox="0 0 720 411" preserveAspectRatio="none" aria-hidden="true">
      <path d="M520 411 C560 250 640 120 720 80 L720 411 Z" fill="var(--green-pale)"/>
      <path d="M560 411 C595 270 660 160 720 125 L720 411 Z" fill="var(--green)"/>
    </svg>
    <div class="brand">
      <span class="brand-dot"></span>
      <h1 class="brand-name">THORNQUIST<br>LANDSCAPING</h1>
    </div>
  </section>

  <section class="card card-back" aria-label="Card back">
    <div class="owner">
      <h2 class="owner-name">MALCOLM THORNQUIST</h2>
      <div class="owner-rule"><span></span><p class="owner-title">OWNER</p></div>
    </div>

    <svg class="back-decoration" viewBox="0 0 250 411" preserveAspectRatio="none" role="img" aria-label="White leaf sprig and grass decoration">
      <path d="M130 0 L250 0 L250 411 L170 411 C150 330 140 250 170 190 C150 130 120 70 130 0 Z" fill="var(--white)" opacity=".92"/>
    </svg>

    <ul class="contact">
      <li>
        <svg viewBox="0 0 24 24" aria-hidden="true"><path fill="#fff" d="M6.6 10.8a15 15 0 0 0 6.6 6.6l2.2-2.2a1 1 0 0 1 1-.25 11.4 11.4 0 0 0 3.6.57 1 1 0 0 1 1 1V20a1 1 0 0 1-1 1A17 17 0 0 1 3 4a1 1 0 0 1 1-1h3.5a1 1 0 0 1 1 1c0 1.25.2 2.45.57 3.570a1 1 0 0 1-.25 1z"/></svg>
        555-782-4610
      </li>
      <li>
        <svg viewBox="0 0 24 24" aria-hidden="true"><path fill="#fff" d="M2 5h20v14H2z"/><path fill="none" stroke="#5bbd2b" stroke-width="1.8" d="M2.5 5.5 12 13l9.5-7.5"/></svg>
        MALCOLMRTHORNQUIST@FERNMAIL.EXAMPLE
      </li>
    </ul>
  </section>

</main>
</body>
</html>
```